Business card design for a engineering company

I need a double sided business card design for my company "Velbrook Stream Systems". The card will be used in Malaysia. Sleek and professional, with a little design flare to it.
Information to showcase:
1. Company logo
2. Name, title, phone, email address, website address
3. our products "Pumping technology, Valve & actuation, Air Moving Technology
Example:
Mark Dovan
Business manager
mark.dovan@velbrook-example.com
www.velbrook-example.com.my
- Pumping technology
- Valve & actuation
- Air moving technology
Target Market(s)
engineers, purchasing managers
Industry/Entity Type
Business
Contact Information for Business Card
Mark Dovan
Business manager
mark.dovan@velbrook-example.com
www.velbrook-example.com.my
- Pumping technology
- Valve & actuation
- Air moving technology
catch phrase : "Solving flow challenges, exceeding expectations"

```html
<!DOCTYPE html>
<html lang="en">
<head>
<meta charset="utf-8">
<title>Velbrook Stream Systems – Business Card</title>
<link href="https://fonts.googleapis.com/css2?family=Open+Sans:wght@300;400;600;700&display=swap" rel="stylesheet">
<style>
  :root {
    --canvas: #e3e4e6;
    --card-white: #ffffff;
    --navy: #123042;
    --navy-soft: #1c4255;
    --orange: #f07a2a;
    --pale-grey: #eceef0;
    --pale-peach: #fdf1e4;
    --rule: #55636c;
  }
  * { box-sizing: border-box; margin: 0; padding: 0; }
  html, body {
    width: 1200px; height: 800px; overflow: hidden;
    background: var(--canvas);
    font-family: "Open Sans", sans-serif;
  }
  .stage {
    position: relative; width: 1200px; height: 800px;
    display: flex; align-items: center; justify-content: center; gap: 50px;
  }
  .card {
    position: relative; width: 540px; height: 310px; overflow: hidden;
    box-shadow: 0 12px 30px rgba(0,0,0,0.14);
  }

  /* Front side */
  .card--front { background: var(--card-white); }
  .front__band {
    position: absolute; left: 0; top: 0; width: 200px; height: 310px;
    background: var(--pale-grey);
  }
  .front__block {
    position: absolute; left: 60px; top: 150px; width: 150px; height: 160px;
    background: var(--pale-peach);
  }
  .wordmark {
    position: absolute; display: flex; align-items: center; gap: 10px;
    font-weight: 700; letter-spacing: 0.02em; line-height: 1.05;
  }
  .front__wordmark { left: 28px; top: 96px; color: var(--navy); font-size: 22px; }
  .wordmark__dot {
    width: 26px; height: 26px; border-radius: 50%; background: var(--orange); flex: none;
  }
  .front__divider {
    position: absolute; left: 262px; top: 60px; width: 1px; height: 190px;
    background: var(--rule);
  }
  .contact { position: absolute; left: 282px; top: 86px; color: var(--navy); }
  .contact__name { font-size: 24px; color: var(--orange); line-height: 1.1; }
  .contact__first { font-weight: 700; }
  .contact__last { font-weight: 300; }
  .contact__title { font-size: 14px; font-weight: 400; margin: 2px 0 14px; }
  .contact__list { list-style: none; font-size: 12px; line-height: 1.6; }
  .contact__label { color: var(--orange); margin-right: 4px; }

  /* Back side */
  .card--back { background: var(--navy); color: #fff; }
  .back__band {
    position: absolute; left: 0; top: 0; width: 230px; height: 310px;
    background: var(--navy-soft); opacity: 0.6;
  }
  .back__content {
    position: absolute; inset: 0; display: flex; flex-direction: column;
    align-items: center; justify-content: center; gap: 18px;
  }
  .back__wordmark { position: static; color: #fff; font-size: 28px; }
  .back__wordmark .wordmark__dot { width: 32px; height: 32px; background: #fff; }
  .products { text-align: center; font-size: 13px; line-height: 1.6; font-weight: 400; }
</style>
</head>
<body>
<main class="stage">
  <section class="card card--front" aria-label="Business card front">
    <div class="front__band"></div>
    <div class="front__block"></div>
    <div class="wordmark front__wordmark">
      <span class="wordmark__dot"></span>
      <span>Velbrook<br>Stream Systems</span>
    </div>
    <div class="front__divider"></div>
    <div class="contact">
      <p class="contact__name"><span class="contact__first">Mark</span> <span class="contact__last">Dovan</span></p>
      <p class="contact__title">Business Manager</p>
      <ul class="contact__list">
        <li><span class="contact__label">T.</span>xxx.xxxxx.xx</li>
        <li><span class="contact__label">E.</span>mark.dovan@velbrook-example.com</li>
        <li><span class="contact__label">W.</span>www.velbrook-example.com.my</li>
      </ul>
    </div>
  </section>

  <section class="card card--back" aria-label="Business card back">
    <div class="back__band"></div>
    <div class="back__content">
      <div class="wordmark back__wordmark">
        <span class="wordmark__dot"></span>
        <span>Velbrook Stream Systems</span>
      </div>
      <p class="products">Pumping technology<br>Valve &amp; actuation | Air moving technology</p>
    </div>
  </section>
</main>
</body>
</html>
```